Staff Newsletter Template Image

We are looking for two .jpg images that we can put into a Word document and use for our staff newsletter. We will then add content using text boxes.
Attached is the current template which works for the columns and size that we need but we just want a fresh new design.
The Word document shows how we use it.
The name will stay the same - Team upBeat but can be a different look to the current one.

Target Market(s)

Sales team

Colors

Designer to choose colors to be used in the design.

Requirements
Must have
• Colours will be green, grey and white, possibly cream if needed. All from the guidelines.
• I have attached our brand guidelines which shows design elements and fonts for our brand. Also attached is brand guidelines for one of our product lines as we would like to use the same green.
• It needs to be nice to look at and motivational for our team

```html
<!DOCTYPE html>
<html lang="en">
<head>
<meta charset="utf-8">
<title>Team upBeat – Staff Newsletter</title>
<link href="https://fonts.googleapis.com/css2?family=Jost:wght@400;500&display=swap" rel="stylesheet">
<style>
  :root {
    --green: #8dc63f;
    --charcoal: #3a3738;
    --white: #ffffff;
    --body-grey: #a0a0a0;
    --footer-text: #c4c4c4;
    --backdrop: #4b4b4b;
  }
  * { margin: 0; padding: 0; box-sizing: border-box; }
  html, body { width: 1200px; height: 960px; overflow: hidden; }
  body {
    background: var(--backdrop);
    font-family: 'Jost', sans-serif;
    position: relative;
  }
  .page-slot { position: absolute; top: 147px; width: 472px; height: 667px; overflow: hidden; }
  .page-slot.front { left: 80px; }
  .page-slot.back { left: 633px; }
  .page {
    position: absolute; left: 0; top: 0;
    width: 848px; height: 1198px;
    transform: scale(0.5566);
    transform-origin: 0 0;
    background: var(--white);
  }
  .page-shapes { position: absolute; inset: 0; width: 100%; height: 100%; }
  .abs { position: absolute; }

  /* front page */
  .brand-name {
    left: 85px; top: 78px;
    font-size: 50px; font-weight: 500; color: var(--green);
    letter-spacing: 0.5px;
  }
  .issue-date { left: 565px; top: 52px; font-size: 33px; color: var(--white); }
  .feature-card {
    left: 49px; top: 250px; width: 749px; height: 455px;
    background: var(--white);
    box-shadow: 0 3px 6px rgba(0,0,0,0.18);
    padding: 28px 34px 0 34px;
  }
  .feature-card p {
    font-size: 18.6px; line-height: 30.8px; color: var(--body-grey);
    margin-bottom: 12px;
  }
  .green-panel {
    top: 750px; width: 367px; height: 278px;
    background: var(--green); text-align: center; color: #1e1e1e;
  }
  .top-sellers { left: 44px; padding: 12px 14px 0; }
  .top-tip { left: 431px; padding: 12px 22px 0; }
  .panel-title { font-size: 21px; font-weight: 400; line-height: 28px; margin-bottom: 6px; }
  .top-tip .panel-title { font-size: 19.5px; font-weight: 500; margin-bottom: 8px; }
  .panel-text { font-size: 16.8px; line-height: 28.8px; }
  .panel-text .emphasis { font-weight: 500; text-decoration: underline; }
  .sellers-table {
    margin-top: 15px; width: 340px;
    border-collapse: separate; border-spacing: 0 0;
    font-size: 18px; color: var(--green);
  }
  .sellers-table td, .sellers-table th {
    background: var(--white); font-weight: 400;
    border: 2px solid var(--green); height: 31px; padding: 0;
  }
  .sellers-table .rank { width: 48px; }
  .shout-out { left: 126px; top: 1078px; width: 200px; text-align: center; color: var(--footer-text); }
  .shout-out .label { font-size: 19px; text-decoration: underline; line-height: 30px; }
  .shout-out .name { font-size: 16px; line-height: 28px; }
  .shout-out .comments { font-size: 14px; line-height: 24px; }
  .copyright { top: 1120px; font-size: 15.5px; color: var(--footer-text); text-align: center; }
  .front .copyright { left: 430px; width: 370px; }
  .back .copyright { left: 0; width: 848px; }

  /* back page */
  .news-column {
    top: 35px; width: 355px; height: 669px; background: var(--white);
  }
  .news-column.left { left: 42px; }
  .news-column.right { left: 449px; }
  .column-head {
    height: 68px; background: var(--charcoal); color: var(--white);
    font-size: 32px; font-weight: 400; text-align: center; line-height: 70px;
  }
  .column-body {
    padding: 33px 30px 0 33px;
    font-size: 18.6px; line-height: 30.8px; color: var(--body-grey);
  }
  .note-block { top: 760px; width: 380px; text-align: center; color: var(--white); }
  .note-block.left { left: 40px; }
  .note-block.right { left: 425px; }
  .note-block h3 { font-size: 19.5px; font-weight: 500; line-height: 30px; margin-bottom: 2px; }
  .note-block p { font-size: 16.8px; line-height: 28.6px; }
  .note-block.right p { margin-top: 5px; }
</style>
</head>
<body>

<div class="page-slot front">
  <section class="page front">
    <svg class="page-shapes" viewBox="0 0 848 1198" preserveAspectRatio="none" aria-hidden="true">
      <rect x="0" y="0" width="848" height="195" fill="var(--green)"/>
      <path d="M0 30 H365 C410 30 430 50 455 85 C475 112 490 117 520 118 L848 124 V195 H0 Z" fill="var(--white)"/>
      <rect x="0" y="195" width="848" height="297" fill="var(--green)"/>
      <rect x="0" y="1063" width="848" height="135" fill="var(--charcoal)"/>
    </svg>

    <div class="abs brand-name">Team upBeat</div>
    <div class="abs issue-date">2019/12/15</div>

    <article class="abs feature-card">
      <p>Lorem ipsum dolor sit amet, consectetur adipiscing elit, sed do eiusmod tempor incididunt ut labore et dolore magna aliqua. Ut enim ad minim veniam, quis nostrud exercitation ullamco laboris nisi ut aliquip ex ea commodo consequat. Duis aute irure dolor in reprehenderit in voluptate velit esse cillum dolore eu fugiat nulla pariatur. Excepteur sint occaecat cupidatat non proident, sunt in culpa qui officia deserunt mollit anim id est laborum.</p>
      <p>Lorem ipsum dolor sit amet, consectetur adipiscing elit, sed do eiusmod tempor incididunt ut labore et dolore magna aliqua. Ut enim ad minim veniam, quis nostrud exercitation ullamco laboris nisi ut aliquip ex ea commodo consequat. Duis aute irure dolor in reprehenderit in voluptate velit esse cillum dolore eu fugiat nulla pariatur. Excepteur sint occaecat cupidatat non proident, sunt in culpa qui officia deserunt mollit anim id est laborum.</p>
    </article>

    <div class="abs green-panel top-sellers">
      <h2 class="panel-title">TOP SELLERS!</h2>
      <p class="panel-text">The following upBeat team members<br>were our top sellers last week<br><span class="emphasis">based on completed sales</span></p>
      <table class="sellers-table">
        <tr><th class="rank">#</th><th>Team Member</th></tr>
        <tr><td class="rank">1</td><td>-100 upBeat Dollars</td></tr>
        <tr><td class="rank">2</td><td>-50 upBeat Dollars</td></tr>
        <tr><td class="rank">3</td><td>-25 upBeat Dollars</td></tr>
      </table>
    </div>

    <div class="abs green-panel top-tip">
      <h2 class="panel-title">Top Tip From our Week’s Top Seller</h2>
      <p class="panel-text">Lorem ipsum dolor sit amet, consectetur adipiscing elit, sed do eiusmod tempor incididunt ut labore et dolore magna aliqua. Ut enim ad minim veniam, quis nostrud exercitation ullamco laboris nisi ut aliquip ex ea commodo consequat.</p>
    </div>

    <div class="abs shout-out">
      <div class="label">Shout Out</div>
      <div class="name">★ Name ★</div>
      <div class="comments">[Comments]</div>
    </div>
    <div class="abs copyright">Copyright 2019. Team upBeat. All Rights Reserved.</div>
  </section>
</div>

<div class="page-slot back">
  <section class="page back">
    <svg class="page-shapes" viewBox="0 0 848 1198" preserveAspectRatio="none" aria-hidden="true">
      <rect x="0" y="0" width="848" height="1063" fill="var(--green)"/>
      <rect x="0" y="1063" width="848" height="135" fill="var(--charcoal)"/>
    </svg>

    <article class="abs news-column left">
      <h2 class="column-head">Company News</h2>
      <p class="column-body">Lorem ipsum dolor sit amet, consectetur adipiscing elit, sed do eiusmod tempor incididunt ut labore et dolore magna aliqua. Ut enim ad minim veniam, quis nostrud exercitation ullamco laboris nisi ut aliquip ex ea commodo consequat. Duis aute irure dolor in reprehenderit in voluptate velit esse cillum dolore eu fugiat nulla pariatur. Excepteur sint occaecat cupidatat non proident, sunt in culpa qui officia deserunt mollit anim id est laborum.</p>
    </article>

    <article class="abs news-column right">
      <h2 class="column-head">Tips &amp; Hints</h2>
      <p class="column-body">Lorem ipsum dolor sit amet, consectetur adipiscing elit, sed do eiusmod tempor incididunt ut labore et dolore magna aliqua. Ut enim ad minim veniam, quis nostrud exercitation ullamco laboris nisi ut aliquip ex ea commodo consequat. Duis aute irure dolor in reprehenderit in voluptate velit esse cillum dolore eu fugiat nulla pariatur. Excepteur sint occaecat cupidatat non proident, sunt in culpa qui officia deserunt mollit anim id est laborum.</p>
    </article>

    <div class="abs note-block left">
      <h3>Reminders</h3>
      <p>Lorem ipsum dolor sit amet, consectetur adipiscing elit, sed do eiusmod tempor incididunt ut labore et dolore magna aliqua. Ut enim ad minim veniam, quis nostrud exercitation ullamco laboris nisi ut aliquip ex ea commodo consequat. Duis aute irure dolor in reprehenderit in voluptate velit esse cillum dolore eu fugiat nulla pariatur.</p>
    </div>

    <div class="abs note-block right">
      <h3>Being an upBeat Team Member Means…</h3>
      <p>Lorem ipsum dolor sit amet, consectetur adipiscing elit, sed do eiusmod tempor incididunt ut labore et dolore magna aliqua. Ut enim ad minim veniam, quis nostrud exercitation ullamco laboris nisi ut aliquip ex ea commodo consequat. Duis aute irure dolor in reprehenderit in voluptate velit esse cillum dolore eu fugiat nulla pariatur.</p>
    </div>

    <div class="abs copyright">Copyright 2019. Team upBeat. All Rights Reserved.</div>
  </section>
</div>

</body>
</html>
```